Pricing and Packages Page

#1 Just looking for a design no coding
We Are looking for a Design of the PRICING AND PACKAGES page. The home page is just for reference material.
Winner will be contacted and possibly hired to do additional jobs.
Brivo Real Estate needs a web page design for our bundles. We need it to be visually appeal and an emphasis placed on the premium bundle. Attached are some pngs of our current page, and a paint mock up of an idea of our layout. Please try and stay within the theme of the top menu bars of the paint file. Whites, Blues, Oranges, and Light Grays would be preferred.
Provided is a mock-up of our home screen. We want easy to read yet an initiative for people to select home listing packages on our website. Possible reference websites would be dwellmart.example and listyourplace.example or any website that has packages and pricing to choose from.
The top of the page should include the title Packages & Pricing.
Below that we want to have it easily read and illustrated that the will "Pay Nothing Until Home Sold"
Next to that a space to enter a anticipated sales price, asking the question, how much will you save. Much sure this is emphasized.
Include the bundles, which are separated into three packages, Basic, Premium and Multi-List Package. Please include the Bundle Prices of $179, $249 and $499 along with + Transaction Coordination Fee $299. Have a spot for a Get Started Button.
The boxes on the side are just an example of what to include with the prices.
Transaction Coordination Fee and All Listings Include, We just want the text display in a way where the page isnt text heavy but illustrated.
Additional Services Offered, Just a basic list with prices next to it.
Paint

```html
<!DOCTYPE html>
<html lang="en">
<head>
<meta charset="utf-8">
<title>Brivo Real Estate — Packages &amp; Pricing</title>
<link href="https://fonts.googleapis.com/css2?family=Open+Sans:wght@400;600;700;800&display=swap" rel="stylesheet">
<style>
:root{
  --navy:#0f3a73;
  --blue:#1e6fc4;
  --blue-light:#3d8ee0;
  --orange:#f38b1c;
  --orange-dark:#e07610;
  --ink:#2b2f36;
  --muted:#7a828d;
  --line:#dfe3e8;
  --page:#f2f4f6;
  --white:#ffffff;
  --dark:#2a2f36;
}
*{box-sizing:border-box;margin:0;padding:0}
html,body{width:698px;height:1200px;overflow:hidden;background:var(--white)}
body{font-family:"Open Sans",Arial,sans-serif;color:var(--ink);font-size:7px;position:relative}
.sec{position:absolute;left:0;width:698px}
.topnav{top:0;height:16px;background:var(--navy);display:flex;align-items:center;padding:0 12px;color:#cfe0f5;font-size:5.5px;font-weight:600;letter-spacing:.3px}
.topnav a{margin-right:14px;color:inherit;text-decoration:none}
.topnav .right{margin-left:auto;display:flex;align-items:center;gap:6px}
.topnav .phone{color:var(--white);font-weight:700;font-size:6.5px}
.topnav .cta{background:var(--orange);color:var(--white);padding:3px 6px;font-size:5px}
.header{top:16px;height:40px;display:flex;align-items:center;padding:0 14px;border-bottom:1px solid var(--line)}
.brand{display:flex;align-items:center;gap:5px;font-size:13px;font-weight:700;color:var(--blue)}
.brand .mark{width:12px;height:12px;background:var(--orange)}
.user{margin-left:auto;display:flex;align-items:center;gap:5px;font-size:6px;font-weight:700}
.avatar{width:16px;height:16px;border-radius:50%;background:linear-gradient(#b9c6d4,#8b9aab)}
.user .name{border:1px solid var(--line);padding:3px 6px}
.hero{top:57px;height:113px;padding:14px 33px}
.hero h1{font-size:10px;font-weight:700}
.pay{display:flex;align-items:center;gap:8px;margin-top:10px}
.pay .coin{width:26px;height:26px;border-radius:50%;background:var(--orange);color:var(--white);font-weight:800;font-size:14px;display:flex;align-items:center;justify-content:center}
.pay p{font-size:10px;font-weight:700;color:var(--blue);line-height:1.2}
.saver{position:absolute;left:278px;top:14px;width:380px}
.saver h2{font-size:10px;font-weight:700}
.saver h3{font-size:8px;font-weight:600;color:var(--blue);margin-top:6px}
.inputs{display:flex;gap:6px;margin-top:6px}
.inputs div{height:16px;border:1px solid var(--line);background:var(--white);font-size:5.5px;color:var(--muted);padding:4px 5px}
.inputs .price{width:160px}.inputs .save{width:110px}
.saver small{display:block;font-size:5.5px;color:var(--muted);margin-top:4px}
.pricing{top:170px;height:382px;background:var(--page)}
.table-card{position:absolute;left:33px;top:16px;width:363px;background:var(--white);border:1px solid var(--line)}
table{border-collapse:collapse;width:100%}
th,td{border-bottom:1px solid var(--line);border-right:1px solid var(--line);font-size:5.5px;text-align:center;height:37px}
tr:last-child td{border-bottom:none}
th:last-child,td:last-child{border-right:none}
td:first-child{text-align:left;padding:0 6px;width:123px;font-weight:600}
th{height:50px;font-weight:700;vertical-align:bottom;padding-bottom:6px}
th .tag{display:block;font-size:4.5px;color:var(--muted);font-weight:600;margin-bottom:4px}
th .amt{display:block;color:var(--orange);font-size:7px;margin-top:2px}
th.basic{color:var(--blue)}
th.premium,td.premium{background:#fff7ee}
td .x{font-size:8px;font-weight:700}
td small{display:block;color:var(--muted);font-size:4.5px;font-weight:400}
.btn{display:inline-block;background:var(--dark);color:var(--white);font-size:5px;font-weight:700;padding:4px 6px}
.note{position:absolute;left:33px;top:370px;font-size:5px;color:var(--muted)}
.side{position:absolute;left:414px;top:16px;width:266px}
.side h2{font-size:9px;font-weight:700}
.bundles{display:flex;gap:8px;margin-top:8px}
.bundle{flex:1;height:64px;color:var(--white);text-align:center;padding-top:8px}
.bundle.basic{background:var(--blue)}
.bundle.premium{background:var(--orange)}
.bundle .lbl{font-size:6px;font-weight:700;letter-spacing:.5px}
.bundle .amt{font-size:17px;font-weight:800;line-height:1.2}
.bundle .fee{font-size:5px}
.side h2.tc{margin-top:24px}
.worry{display:flex;gap:10px;margin-top:10px;align-items:flex-start}
.worry .badge{width:46px;height:36px;border:2px solid var(--dark);display:flex;align-items:center;justify-content:center;font-size:7px;font-weight:800;text-align:center;line-height:1;flex:none}
.worry p{font-size:5.5px;color:var(--muted);line-height:1.5}
.features{top:552px;height:150px;padding:18px 33px}
.sec h2.title{font-size:10px;font-weight:700;border-bottom:1px solid var(--line);padding-bottom:6px}
.grid{display:grid;grid-template-columns:repeat(3,1fr);row-gap:18px;margin-top:16px;padding-left:30px}
.feat{display:flex;align-items:center;gap:8px;font-size:6px;font-weight:600;line-height:1.3}
.feat svg{width:20px;height:20px;flex:none}
.services{top:702px;height:213px;padding:6px 33px}
.services .hint{font-size:5px;color:var(--muted);margin-top:4px}
.ask{display:flex;align-items:center;gap:6px;font-size:7px;font-weight:600;color:var(--blue);margin-top:8px}
.ask .box{width:8px;height:8px;border:1px solid var(--muted);background:var(--white)}
.svc{width:300px;margin-top:10px}
.svc .row{display:grid;grid-template-columns:150px 100px 50px;align-items:center;height:19px;border-bottom:1px solid var(--line);font-size:5.5px}
.svc .head{font-weight:700;color:var(--blue);border-bottom:2px solid var(--blue);font-size:6px}
.plus{width:9px;height:9px;border-radius:50%;background:var(--dark);color:var(--white);font-size:7px;line-height:9px;text-align:center;font-weight:700}
.browse{top:915px;height:142px;background:var(--page);padding:14px 33px}
.browse h2{font-size:9px;font-weight:800}
.cities{display:grid;grid-template-columns:repeat(4,74px);margin-top:8px;font-size:5px;line-height:1.75;color:var(--muted)}
.viewall{font-size:5.5px;font-weight:700;color:var(--blue);margin-top:8px}
.how{position:absolute;left:430px;top:14px}
.video{width:200px;height:90px;margin-top:8px;background:linear-gradient(135deg,#6f8a5c,#3f5a7a)}
.skyline{top:1057px;height:38px}
.footer{top:1095px;height:83px;background:var(--navy);padding:12px 33px;color:#c9d9ee;display:flex;gap:38px;font-size:5px;line-height:1.8}
.footer b{color:var(--white);font-size:5.5px}
.news{margin-left:auto;width:190px}
.news .field{display:flex;margin-top:4px}
.news .field span{flex:1;height:13px;background:var(--white)}
.news .field i{width:22px;height:13px;background:var(--orange)}
.social{display:flex;gap:4px;margin-top:8px}
.social span{width:12px;height:12px;background:var(--blue-light)}
.copy{top:1178px;height:22px;background:#0a2c58;color:#8ea8c8;font-size:5px;display:flex;align-items:center;justify-content:space-between;padding:0 33px}
</style>
</head>
<body>

<nav class="sec topnav">
  <a>SEARCH LISTINGS</a><a>WHY CHOOSE BRIVO?</a><a>DIRECTORY</a><a>GUIDES</a>
  <div class="right"><span class="phone">1-800-555-0134</span><span class="cta">SELL | CONTACT US | FAQ</span></div>
</nav>

<header class="sec header">
  <div class="brand"><span class="mark"></span>Brivo Real Estate</div>
  <div class="user"><span class="avatar" role="img" aria-label="Member profile photo"></span><span class="name">JORDAN K ▾</span></div>
</header>

<section class="sec hero">
  <h1>Packages &amp; Pricing</h1>
  <div class="pay"><span class="coin">$</span><p>Pay Nothing<br>Until Home<br>Sold !</p></div>
  <div class="saver">
    <h2>Maximum Market Exposure Guaranteed !</h2>
    <h3>How Much Will You Save ?</h3>
    <div class="inputs"><div class="price">$</div><div class="save">No savings...</div></div>
    <small>Enter Estimated Sales Price</small>
  </div>
</section>

<section class="sec pricing">
  <div class="table-card">
    <table>
      <tr><th></th><th class="basic"><span class="tag">&nbsp;</span>BASIC<span class="amt">$179</span></th><th class="premium"><span class="tag">MOST POPULAR</span>PREMIUM<span class="amt">$249</span></th><th>MLS<span class="amt">$499</span></th></tr>
      <tr><td>Listing on BrivoRealEstate.com</td><td><span class="x">X</span></td><td class="premium"><span class="x">X</span></td><td><span class="x">X</span></td></tr>
      <tr><td>Each Featured Listing on BrivoRealEstate.com</td><td><span class="x">X</span></td><td class="premium"><span class="x">X</span></td><td><span class="x">X</span></td></tr>
      <tr><td>Photos</td><td><span class="x">5</span></td><td class="premium">Unlimited</td><td>Unlimited</td></tr>
      <tr><td>Free Brokers Price Opinion</td><td></td><td class="premium"><span class="x">X</span></td><td><span class="x">X</span></td></tr>
      <tr><td>Exposure On Over 100+ Real Estate Websites Including:<small>• Major home portals<br>• Local listing sites</small></td><td></td><td class="premium"><span class="x">X</span></td><td><span class="x">X</span></td></tr>
      <tr><td>Premium Yard Sign With Rider &amp; Flyer Box</td><td></td><td class="premium"><span class="x">X</span></td><td><span class="x">X</span></td></tr>
      <tr><td>Listing On Local MLS</td><td></td><td class="premium"></td><td><span class="x">X</span></td></tr>
      <tr><td></td><td><span class="btn">Get Started</span></td><td class="premium"><span class="btn">Get Started</span></td><td><span class="btn">Get Started</span></td></tr>
    </table>
  </div>
  <p class="note">* All packages + $299 transaction coordination fee</p>
  <aside class="side">
    <h2>Best Value</h2>
    <div class="bundles">
      <div class="bundle basic"><div class="lbl">BASIC</div><div class="amt">$ 179</div><div class="fee">+ Transaction Coordination<br>Fee $299</div></div>
      <div class="bundle premium"><div class="lbl">PREMIUM</div><div class="amt">$ 249</div><div class="fee">+ Transaction Coordination<br>Fee $299</div></div>
    </div>
    <h2 class="tc">Transaction Coordination Fees</h2>
    <div class="worry">
      <div class="badge">NO<br>WORRIES</div>
      <p>For the transaction coordination, Brivo Real Estate will guide the buyer and seller through the entire transaction in an efficient and worry-free way.</p>
    </div>
  </aside>
</section>

<section class="sec features">
  <h2 class="title">All Listing Included</h2>
  <div class="grid">
    <div class="feat"><svg viewBox="0 0 20 20" fill="none" stroke="#1e6fc4" stroke-width="1.6"><path d="M3 9l7-6 7 6v8H3z"/><path d="M8 17v-5h4v5"/></svg>Help Pre- Approved<br>Buyers</div>
    <div class="feat"><svg viewBox="0 0 20 20" fill="none" stroke="#1e6fc4" stroke-width="1.6"><rect x="3" y="4" width="14" height="13"/><path d="M3 8h14M7 2v4M13 2v4"/></svg>Schedule Open<br>Houses</div>
    <div class="feat"><svg viewBox="0 0 20 20" fill="none" stroke="#1e6fc4" stroke-width="1.6"><path d="M5 3h3l1 4-2 1a9 9 0 0 0 5 5l1-2 4 1v3a2 2 0 0 1-2 2A14 14 0 0 1 3 5a2 2 0 0 1 2-2z"/></svg>Customer Support 7<br>Days a Week</div>
    <div class="feat"><svg viewBox="0 0 20 20" fill="none" stroke="#1e6fc4" stroke-width="1.6"><path d="M5 2h7l4 4v12H5z"/><path d="M8 9h5M8 12h5M8 15h3"/></svg>Contract Negotiation<br>Support</div>
    <div class="feat"><svg viewBox="0 0 20 20" fill="none" stroke="#1e6fc4" stroke-width="1.6"><path d="M4 16l8-8M12 8a3 3 0 1 0 3-5l-2 2-1-1 2-2"/><path d="M13 13l4 4M9 11l5 5"/></svg>Step by Step<br>Guide &amp; Tools</div>
    <div class="feat"><svg viewBox="0 0 20 20" fill="none" stroke="#1e6fc4" stroke-width="1.6"><path d="M3 17h14M5 14v-4M9 14V6M13 14v-6M17 14V3"/></svg>Listing Stats<br>Tracking</div>
  </div>
</section>

<section class="sec services">
  <h2 class="title">Additional Services Offered</h2>
  <p class="hint">* Payment due when service is completed</p>
  <div class="ask">Will you offer a 3% buyers agent commission ? <span class="box"></span></div>
  <div class="svc">
    <div class="row head"><span>SERVICE</span><span>PRICE</span><span></span></div>
    <div class="row"><span>Professional Photography</span><span>$ xxx</span><span class="plus">+</span></div>
    <div class="row"><span>Professional Home Staging</span><span>$ xxx</span><span class="plus">+</span></div>
    <div class="row"><span>Broker Price Opinion</span><span>$ xxx</span><span class="plus">+</span></div>
    <div class="row"><span>Premium Yard Sign</span><span>$ xxx</span><span class="plus">+</span></div>
  </div>
</section>

<section class="sec browse">
  <h2>BROWSE BY CITIES</h2>
  <div class="cities">
    <div>New york<br>Los Angeles<br>Chicago<br>Miami<br>San Francisco<br>Denver</div>
    <div>New york<br>Los Angeles<br>Chicago<br>Miami<br>San Francisco<br>Denver</div>
    <div>New york<br>Los Angeles<br>Chicago<br>Miami<br>San Francisco<br>Denver</div>
    <div>New york<br>Los Angeles<br>Chicago<br>Miami<br>San Francisco<br>Denver</div>
  </div>
  <p class="viewall">VIEW ALL CITIES »</p>
  <div class="how">
    <h2>HOW IT WORKS</h2>
    <div class="video" role="img" aria-label="Video preview of a home with a for-sale sign"></div>
  </div>
</section>

<div class="sec skyline" role="img" aria-label="City skyline silhouette band" style="background:linear-gradient(#ffffff,#9fc3ea 55%,#3d8ee0)"></div>

<footer class="sec footer">
  <div><b>About</b><br>Research<br>Sponsors<br>Contact Us<br>Why Choose Us</div>
  <div><b>Search Listings</b><br>Real Estate Guide<br>Neighborhoods<br>List For Appraisal<br>The Housing Care &amp; Information</div>
  <div><b>Disclosures</b><br>Feedback<br>Terms &amp; Conditions<br>Help</div>
  <div class="news"><b>Enter your email address to sign for our newsletter</b>
    <div class="field"><span></span><i></i></div>
    <div class="social"><span></span><span></span><span></span><span></span></div>
  </div>
</footer>
<div class="sec copy"><span>© 2024 Brivo Real Estate. All rights reserved.</span><span>Privacy | Terms of use</span></div>

</body>
</html>
```